Wordpress Layout, Plug-in, Mash-up Overhaul

We have collection of vertical topic portals; in each portal, a post typically is an article which goes with a subject video, following are 5 reference sites:

http://www.ledgerbrook.com/
http://www.velmacounsel.com/
http://www.shimmerlane.tv/
http://www.nestharbor.com/
http://www.ladiestalkly.com/

We obtained most of our based WP theme from various premium WP template membership sites, subsequently re-organise, mash-up content to produce sites as above; however we start to be constraint as we get into a fixed pattern of laying out our contents and we seeking professional help to re-work this. these re-work can includes as follows.

1. proposal on creative re-placement of component / re-layout on the templates. Should also suggest different way for the advertising banner placement etc.

2. proposal on right and appropriate use of WP plugins (paid or free but have to be secured and reliable) to achieve more relevant add-on of content where necessary (rss, etc)

Objective:
We want to move away from our internal team design constraint and also moving alway from being stuck with certain stereo-type way of WP content site. However the proposed WP design should still be a portal-centric type vs blogging/product-centric.

Deliverables:
1. We don't need the actual cut template but a design mockup of the home page and relevant sub pages (.psd, jpg etc) for the proposed re-design. Based on the above 5 listed sites, the deliverable would be at least 10 pages of design layout work (considering home page and 1 sub pages for each domain; could be more if necessary)

2. The plugins reference where necessary

What's expected from your proposal for the bid:
We would like a mockup of a re-design from any pick from any of the above 5 domains

```html
<!DOCTYPE html>
<html lang="en">
<head>
<meta charset="utf-8">
<title>Ledgerbrook Finance</title>
<link href="https://fonts.googleapis.com/css2?family=Open+Sans:wght@400;600;700&family=Arimo:wght@400&display=swap" rel="stylesheet">
<style>
:root{
  --ink:#4a4a4a;
  --body:#5c5c5c;
  --navy:#1f4f86;
  --gold:#f0a800;
  --gold-light:#fcc419;
  --rule:#dddddd;
  --footer:#333333;
  --footer-base:#2b2b2b;
  --footer-text:#e6e6e6;
  --bullet:#1d4a7a;
}
*{margin:0;padding:0;box-sizing:border-box}
html,body{width:925px;height:1200px;overflow:hidden;background:#fff}
body{position:relative;font-family:"Open Sans",sans-serif;color:var(--body)}
.abs{position:absolute}
.topline{left:0;top:0;width:925px;height:4px;background:#222}
.brand{left:109px;top:38px;display:flex;align-items:center;gap:7px}
.brand-mark{width:34px;height:34px;background:var(--navy)}
.brand-name{font-size:17px;font-weight:700;color:var(--navy);line-height:1}
.connect{right:212px;top:31px;font-size:8.5px;font-weight:600;color:var(--navy);letter-spacing:.2px;white-space:nowrap;text-align:right}
.social{display:flex;gap:6px}
.social span{width:20px;height:20px;border-radius:50%;display:block}
.social.top{left:718px;top:25px}
.c-blue{background:#3b5998}.c-sky{background:#29a9e1}.c-navy{background:#0e76a8}.c-orange{background:#f26522}.c-red{background:#dd4b39}
.search{left:634px;top:66px;width:182px;height:23px;border:1px solid #ddd;border-radius:3px;background:#f5f5f5}
.search-btn{right:-1px;top:-1px;width:25px;height:23px;background:#1f4f77;border-radius:0 3px 3px 0;display:flex;align-items:center;justify-content:center}
.nav{left:0;top:112px;width:925px;height:38px;background:linear-gradient(#fcc52a,#f2a900)}
.nav a{position:absolute;top:13px;font-size:10px;font-weight:700;color:#fff;text-decoration:none;text-transform:uppercase;text-shadow:0 1px 1px rgba(0,0,0,.45);white-space:nowrap}
.hero{left:0;top:150px;width:925px;height:315px;background:linear-gradient(100deg,#8a8c8c,#c9c9c7 45%,#b49a5f 70%,#9c9c98)}
.dots{left:420px;top:432px;display:flex;gap:7px}
.dots span{width:7px;height:7px;border-radius:50%;background:#ddd}
.dots span.on{background:var(--gold);box-shadow:0 0 0 2px #fff}
h2.section{font-size:16px;font-weight:600;color:var(--ink);text-transform:uppercase}
h2.section em{font-style:normal;color:var(--gold)}
.rule{height:1px;background:var(--rule)}
.video{left:109px;top:534px;width:217px;height:164px;border:1px solid #ddd;padding:5px}
.video-fill{width:100%;height:100%;background:linear-gradient(120deg,#c6cbd0,#e8e2c4 50%,#8a8f95)}
.play{left:88px;top:58px;width:36px;height:36px;border-radius:50%;background:rgba(90,90,90,.8);border:2px solid #ddd}
.lead{left:361px;top:531px;width:455px;font-size:10px;font-weight:600;line-height:13px;color:var(--ink);text-align:justify}
.copy{left:361px;width:455px;font-size:8.6px;line-height:13px;color:var(--body);text-align:justify}
.col{width:218px}
.col h3{font-size:12px;font-weight:600;color:var(--navy);text-transform:uppercase;height:18px;white-space:nowrap}
.col .rule{margin-top:8px;margin-bottom:13px}
.col p{font-size:8.6px;line-height:13px;text-align:justify}
.list{list-style:none}
.list li{height:26px;border-bottom:1px solid #e6e6e6;display:flex;align-items:center;font-size:8.6px;color:var(--ink)}
.list li svg{margin:0 19px 0 3px;flex:none}
.more{width:47px;height:20px;background:var(--gold);color:#fff;font-size:9px;font-weight:700;display:flex;align-items:center;justify-content:center}
.post{display:flex;gap:11px;height:53px}
.thumb{width:45px;height:45px;border:1px solid #ccc;flex:none}
.post h4{font-size:9.5px;font-weight:400;color:var(--navy);margin-bottom:3px}
.post p{font-size:8.3px;line-height:16px}
.footer{left:0;top:1017px;width:925px;height:149px;background:var(--footer);font-family:Arimo,sans-serif;color:var(--footer-text)}
.footer ul{position:absolute;top:11px;list-style:none;font-size:8.6px}
.footer li{height:21.6px}
.news-title{left:470px;top:9px;font-family:"Open Sans",sans-serif;font-size:11.5px;color:#fff}
.field{left:469px;width:151px;height:23px;background:#fff;border:1px solid #aaa;font-size:8.5px;color:#555;padding:6px 5px}
.signup{left:548px;top:105px;width:72px;height:23px;background:#4a4a4a;color:#fff;font-size:11.5px;display:flex;align-items:center;justify-content:center}
.contact{left:706px;top:10px;font-size:8.6px;line-height:13px}
.social.foot{left:692px;top:111px}
.base{left:0;top:1166px;width:925px;height:34px;background:var(--footer-base);font-family:Arimo,sans-serif;font-size:8.6px;color:#ddd;text-align:center;padding-top:11px}
</style>
</head>
<body>
<svg width="0" height="0" style="position:absolute">
  <defs>
    <symbol id="chev" viewBox="0 0 9 9"><circle cx="4.5" cy="4.5" r="4.5" fill="#1d4a7a"/><polyline points="3.3,2.5 5.4,4.5 3.3,6.5" fill="none" stroke="#fff" stroke-width="1.3"/></symbol>
  </defs>
</svg>
<div class="abs topline"></div>

<div class="abs brand"><span class="brand-mark"></span><span class="brand-name">Ledgerbrook Finance</span></div>
<div class="abs connect">CONNECT WITH LEDGERBROOK FINANCE :</div>
<div class="abs social top"><span class="c-blue"></span><span class="c-sky"></span><span class="c-navy"></span><span class="c-orange"></span></div>
<div class="abs search"><div class="abs search-btn"><svg width="11" height="11" viewBox="0 0 11 11"><circle cx="6.5" cy="4.5" r="3.2" fill="none" stroke="#fff" stroke-width="1.4"/><line x1="4.2" y1="6.8" x2="1" y2="10" stroke="#fff" stroke-width="1.8"/></svg></div></div>

<nav class="abs nav">
  <a style="left:109px">Home</a><a style="left:158px">About Us</a><a style="left:224px">Financial Management</a><a style="left:366px">Insurance</a><a style="left:441px">Investing</a><a style="left:512px">Loans</a><a style="left:562px">Real Estate</a><a style="left:642px">Retirement</a><a style="left:719px">Tax</a><a style="left:754px">Contact Us</a>
</nav>

<div class="abs hero" role="img" aria-label="Businessman relaxing in an office chair with his feet on a tall stack of gold coins beside a large coin"></div>
<div class="abs dots"><span class="on"></span><span></span><span></span><span></span></div>

<h2 class="abs section" style="left:109px;top:495px">How It Works</h2>
<div class="abs rule" style="left:109px;top:523px;width:217px"></div>
<div class="abs video">
  <div class="video-fill" role="img" aria-label="Video still of a financial adviser meeting with a couple"></div>
  <div class="abs play"><svg width="32" height="32" viewBox="0 0 32 32"><polygon points="12,9 12,23 23,16" fill="#eee"/></svg></div>
</div>

<h2 class="abs section" style="left:361px;top:495px">Welcome to <em>Our Company</em></h2>
<div class="abs rule" style="left:361px;top:523px;width:455px"></div>
<p class="abs lead">We are a news source for all things related to business and finance. Our aim is to connect global events to their economic ramifications, giving you the news you need to make the right decisions. In a world of global instability, having news coverage that is fast, thorough, and in-depth is an invaluable asset.</p>
<p class="abs copy" style="top:596px">Sed ut perspiciatis unde omnis iste natus error sit voluptatem accusantium doloremque laudantium, totam rem aperiam, eaque ipsa quae ab illo inventore veritatis et quasi architecto beatae vitae dicta sunt explicabo. Nemo enim ipsam voluptatem quia voluptas sit aspernatur aut odit aut fugit, sed quia consequuntur magni dolores eos qui ratione voluptatem sequi nesciunt.</p>
<p class="abs copy" style="top:661px">Neque porro quisquam est, qui dolorem ipsum quia dolor sit amet, consectetur, adipisci velit, sed quia non numquam eius modi tempora incidunt ut labore et dolore magnam aliquam quaerat voluptatem. Ut enim ad minima veniam, quis nostrum exercitationem ullam corporis suscipit laboriosam, nisi ut aliquid ex ea commodi</p>

<section class="abs col" style="left:110px;top:724px">
  <h3>Financial Management</h3><div class="rule"></div>
  <p>Repaying a loan is one of the most important things that maintain your credit and to give you piece of mind as well. Repaying a loan is [...]</p>
  <ul class="list" style="margin-top:6px">
    <li><svg width="9" height="9"><use href="#chev"/></svg>Repaying A Loan</li><li><svg width="9" height="9"><use href="#chev"/></svg>How To Choose A Loan</li><li><svg width="9" height="9"><use href="#chev"/></svg>Understanding Mortgage Loans</li><li><svg width="9" height="9"><use href="#chev"/></svg>Car Loans</li><li><svg width="9" height="9"><use href="#chev"/></svg>Managing Loans</li><li><svg width="9" height="9"><use href="#chev"/></svg>How To Protect Your Money</li>
  </ul>
</section>
<section class="abs col" style="left:353px;top:724px">
  <h3>Categories</h3><div class="rule" style="margin-bottom:4px"></div>
  <ul class="list">
    <li><svg width="9" height="9"><use href="#chev"/></svg>Financial Management</li><li><svg width="9" height="9"><use href="#chev"/></svg>Insurance</li><li><svg width="9" height="9"><use href="#chev"/></svg>Investing</li><li><svg width="9" height="9"><use href="#chev"/></svg>Insurance</li><li><svg width="9" height="9"><use href="#chev"/></svg>Loans</li><li><svg width="9" height="9"><use href="#chev"/></svg>Real Estate</li><li><svg width="9" height="9"><use href="#chev"/></svg>Retirement</li><li><svg width="9" height="9"><use href="#chev"/></svg>Tax</li>
  </ul>
</section>
<section class="abs col" style="left:597px;top:724px">
  <h3>Recent Posts and Popular Post</h3><div class="rule"></div>
  <p style="padding-left:3px">Repaying a loan is one of the most important things that maintain your credit and to give you piece of mind as well. Repaying a loan is [...]</p>
  <div style="margin-top:9px">
    <div class="post"><div class="thumb" role="img" aria-label="Hands counting banknotes" style="background:linear-gradient(#e3c9a8,#b89c7a)"></div><div><h4>Repaying A Loan</h4><p>There are different variations of home loans that are available.</p></div></div>
    <div class="post"><div class="thumb" role="img" aria-label="Pen resting on financial charts" style="background:linear-gradient(#d8e2c4,#7aa05a)"></div><div><h4>How To Do Financial Planning</h4><p>There are different variations of home loans that are available.</p></div></div>
    <div class="post"><div class="thumb" role="img" aria-label="Padlock on a stack of banknotes" style="background:linear-gradient(#b9c4b0,#5d6b58)"></div><div><h4>How To Protect Your Money</h4><p>There are different variations of home loans that are available.</p></div></div>
  </div>
</section>
<div class="abs more" style="left:110px;top:974px">MORE</div>
<div class="abs more" style="left:353px;top:974px">MORE</div>
<div class="abs more" style="left:597px;top:974px">MORE</div>

<footer class="abs footer">
  <ul style="left:110px"><li>Home</li><li>About</li><li>News</li><li>Services</li><li>What We Do</li><li>Contact Us</li></ul>
  <ul style="left:214px"><li>Grief &amp; Healing</li><li>Resources</li><li>Plan Now</li><li>Locations</li><li>Privacy Policy</li><li>Terms &amp; Conditions</li></ul>
  <ul style="left:341px"><li>Resources</li><li>Plan Now</li><li>Locations</li><li>Privacy Policy</li><li>Terms &amp; Conditions</li></ul>
  <div class="abs news-title">NEWSLETTER SIGN UP</div>
  <div class="abs field" style="top:37px">Enter Name</div>
  <div class="abs field" style="top:69px">Enter Email Address</div>
  <div class="abs signup">SIGN UP</div>
  <div class="abs contact">Shooting Sports<br>Sed ut perspiciatis unde,<br>&nbsp;sit voluptatem a<br><br>Phone: (000) 000 0000<br>Fax: (000) 000 0000</div>
  <div class="abs social foot"><span class="c-blue"></span><span class="c-sky"></span><span class="c-navy"></span><span class="c-red"></span><span class="c-orange"></span></div>
</footer>
<div class="abs base">© 2014 Ledgerbrook Finance. All Rights Reserved.</div>
</body>
</html>
```